Newly created Management Consulting company needs a brochure to capture clients's interest

This is a new management consulting firm providing service in Finance, Marketing, Operations/Manufacturing Strategy, and Project Management.
Please go to the company's website: www.veltanorpartners.ca . The website is pretty straightforward and gives a clear explanation of all the services and sub-services offered. Based on the existent material on the website, I would like to create a company's brochure that can inspire clients to seek our services.
One important thing: the slogan/tagline ("Shaping the future of your business") needs to be added somewhere in the vicinity of our company's' LOGO. Please see attached the company's logo (JPEG file).
The brochure size and number of pages can vary, depending on the layout of the brochure so it can fit the content, so I am open to different and innovative sizes/shapes and no. of pages etc. Graphics should combine real pictures with graphic design technology, and should give a professional look and feel comparable to big companies' marketing materials.
Updates
The brochure does not necessarily have to include pictures that are on the website. If you think that other pictures and graphics can deliver a stronger message to customers, by all means I am open to any other ideas.
Thanks.
As I said before, the pictures do not need to be exactly the same pictures as on the website, if you can bring in other cool pictures to attract clients, please go ahead. Also, you do not need to use only black background, if you have better colors ideas to combine with the our LOGO, and it looks good, by all means do use other colors. But our LOGO needs to be represented as it is on the JPEG I attached.
May the most creative and cool design win! Good luck!
Please ensure that all the content of our website fits into your brochure, including our contact information. It is up to you to come up with the necessary number of pages, design and shape of the brochure, but the text should be clear enough to be read by a normal person without a magnifying glass.
Thank you.
In order to keep the brochure to a reasonable number of pages, I agree that it is not necessary to include 100% all the text that appears on the website. That being said, even if you do not have enough space to include all the background and introduction paragraphs under each service/sub-service, it is still important that the main message for each service/sub-service is being contained in the brochure.
Target Market(s)
Our clients are companies with sizes starting from 10-20 employees and up to large Larkspan 700 companies.
Industry/Entity Type
Management Consulting
Look and feel

```html
<!DOCTYPE html>
<html lang="en">
<head>
<meta charset="utf-8">
<title>Veltanor Partners – Operations Brochure Spread</title>
<link rel="stylesheet" href="https://fonts.googleapis.com/css2?family=Montserrat:wght@700;800&family=Raleway:wght@400;600;700&display=swap">
<style>
  :root{
    --backdrop:#e4e4e4;
    --page:#1d1b1c;
    --page-edge:#141314;
    --text:#d6d6d6;
    --muted:#b9b9b9;
    --green:#1f9e48;
    --green-bright:#6cc04a;
    --white:#ffffff;
  }
  *{box-sizing:border-box;margin:0;padding:0}
  html,body{width:1200px;height:956px;overflow:hidden}
  body{
    background:var(--backdrop);
    font-family:"Raleway",Arial,sans-serif;
    color:var(--text);
    display:flex;align-items:center;justify-content:center;
  }
  .spread{
    width:1100px;height:780px;display:flex;
    box-shadow:0 20px 40px rgba(0,0,0,.25);
  }
  .page{
    width:550px;height:780px;background:var(--page);position:relative;overflow:hidden;
  }
  .page--left{border-right:1px solid var(--page-edge);padding:34px 40px 30px 40px}
  .page--right{background:linear-gradient(90deg,var(--page-edge) 0,var(--page) 24px)}

  .section-tab{
    position:absolute;left:40px;top:26px;
    background:var(--green);color:var(--white);
    font-family:"Montserrat",Arial,sans-serif;font-weight:800;font-size:17px;letter-spacing:.5px;
    padding:9px 36px 9px 34px;border-radius:0 10px 0 0;
  }
  .intro{margin-top:62px}
  p{font-size:9.6px;line-height:13.2px;margin-bottom:11px}
  .lead{color:var(--green-bright);font-weight:700}
  .lead-white{color:var(--white);font-weight:700}

  .tick-list{list-style:none;margin-bottom:11px}
  .tick-list > li{position:relative;padding-left:16px;font-size:9.6px;line-height:13.2px;margin-bottom:10px}
  .tick-list > li::before,
  .capabilities li::before,
  .approach li::before{
    content:"";position:absolute;left:2px;top:2px;width:4px;height:7px;
    border:solid var(--green-bright);border-width:0 2px 2px 0;transform:rotate(45deg);
  }
  .question{margin:8px 0 3px 10px}
  .dot-list{list-style:none;margin-left:20px}
  .dot-list li{position:relative;padding-left:12px;font-size:9.2px;line-height:12.4px}
  .dot-list li::before{
    content:"";position:absolute;left:0;top:3px;width:7px;height:7px;border-radius:50%;
    border:1.5px solid var(--green-bright);
  }
  .capabilities-title{font-size:9.8px;margin:6px 0 2px 10px}
  .capabilities{list-style:none;margin-left:14px}
  .capabilities li{position:relative;padding-left:14px;font-size:9.8px;line-height:13.4px}

  .photo-area{
    height:300px;
    background:linear-gradient(180deg,#b7c0c6 0%,#7b858c 30%,#4a4f53 60%,#1d1b1c 100%);
  }
  .right-body{padding:0 40px 0 44px;margin-top:-6px}
  .service-label{
    display:inline-block;background:var(--green);color:var(--white);
    font-family:"Montserrat",Arial,sans-serif;font-weight:700;font-size:9.6px;
    padding:4px 8px;margin-bottom:12px;letter-spacing:.2px;
  }
  .sub-heading{color:var(--green-bright);font-weight:700;font-size:10px;margin:14px 0 2px}
  .approach{list-style:none;margin:-6px 0 11px 10px}
  .approach li{position:relative;padding-left:14px;font-size:9.6px;line-height:13.2px}
  .highlight{color:var(--green-bright);font-weight:700}
</style>
</head>
<body>
  <main class="spread">
    <section class="page page--left">
      <h1 class="section-tab">OPERATIONS</h1>
      <div class="intro">
        <p>The operations function is uniquely positioned at the heart of your business. Achieving operational excellence will help you run a more efficient business, which lowers costs and improves cycle times. We work closely with clients of all levels – from small business owners to large corporations. Together, we develop solid operations strategies that will develop resources and configure processes, achieving the competitive position the firm is seeking over time.</p>
        <p>Many managers and other consultants think of operations as the planning and the execution of the work. Our consultants will use their industry experience, rigorous analytical capabilities, and a pragmatic mindset to provide a 360-degree perspective on your operations. We will adopt three different, yet complimentary views, of your business operations:</p>
      </div>
      <ul class="tick-list">
        <li><span class="lead">Resources:</span> human resources, capital assets, customers and suppliers relationships, intellectual property, reputation and brands, knowledge and experience in processing, technologies, and markets.
          <p class="question">While developing your organization's resource strategy we will answer questions related to:</p>
          <ul class="dot-list">
            <li>Capacity Sizing - How many resources/capital you should invest in?</li>
            <li>Capacity Timing - When should you increase or reduce resources?</li>
            <li>Capacity Type - What kinds of resources are best?</li>
            <li>Capacity Location - Where should your resources be geographically located?</li>
          </ul>
        </li>
        <li><span class="lead">Processes:</span> The value-added activities such as production, service, administration and support, supply chain, sales, marketing, distribution, etc.
          <p class="question">We will answer key questions related to:</p>
          <ul class="dot-list">
            <li>Supply or Strategic Sourcing - Which activities should you perform internally, which are outsourced, and how do you manage suppliers?</li>
            <li>Technology - Which technologies do your processes need?</li>
            <li>Demand Management - How do you manage demand to available supply?</li>
            <li>Improvement and Innovation - How and when do you need to improve your product and processes?</li>
          </ul>
        </li>
        <li><span class="lead">Competencies:</span> they determine the products or services that the operation of a business is particularly good at providing to its customers. Competencies are the abilities of the business to assemble the resources, processes, and values.
          <p class="question">To determine your organization's competencies we will ask questions related to:</p>
          <ul class="dot-list">
            <li>Cost - What is the total cost of operating, including variable and fixed costs?</li>
            <li>Time - What is the total response or lead time for your products or services?</li>
            <li>Quality - What is your operations' ability to deliver quality products or services?</li>
            <li>Flexibility - What is your operations' flexibility to change regarding inputs, activities, volumes or outputs?</li>
          </ul>
        </li>
      </ul>
      <p class="capabilities-title">Our Capabilities:</p>
      <ul class="capabilities">
        <li>Process Selection and Capacity Planning</li>
        <li>Facilities Layout</li>
        <li>Design of Work System</li>
        <li>Location Planning and Analysis</li>
        <li>Aggregate Planning</li>
        <li>Supply Chain Management</li>
        <li>Strategic Sourcing / Outsourcing</li>
        <li>Capacity Sizing / Investment</li>
      </ul>
    </section>

    <section class="page page--right">
      <div class="photo-area" role="img" aria-label="Photo of an automated factory production line with rows of machined metal parts"></div>
      <div class="right-body">
        <h2 class="service-label">MANUFACTURING STRATEGY SERVICES</h2>
        <p>Manufacturing is complex. In many companies, the manufacturing function struggles to provide what the company needs to be successful. Increasing customer expectations, competitor's capabilities, shifting global economics, and outdated industrial capabilities hinder many manufacturing companies from staying competitive. What they need is strategy that keeps the manufacturing function aligned with a fast marketplace.</p>
        <p>To stay competitive and meet market expectations in a global economy, a company must realign its manufacturing processes, make improvements, and increase its manufacturing capabilities.</p>
        <h3 class="sub-heading">Manufacturing Strategy</h3>
        <p>We work with senior executives, managers, and small business owners to bring about improvements from the tactical to the strategic level of their manufacturing operation. We help formulate a manufacturing strategy that will help their companies achieve a long-term advantage over its competitors. We ensure that our client's strategy focuses on effectiveness first, and then on efficiency. This should ensure that the right things are done, and done well.</p>
        <p>We tailor our solution to the client's situation. The approach may vary from client-to-client, but the overall framework of our process for developing a manufacturing strategy remains the same. We will:</p>
        <ul class="approach">
          <li>Evaluate your factory in terms of the manufacturing outputs it provides and the production system it uses.</li>
          <li>Select the most suitable production system through competitive analysis.</li>
          <li>Examine process improvement programs such as quality management, cycle time reduction, agile manufacturing, and re-engineering.</li>
          <li>Use advanced techniques, such as lean six-sigma, to change your production system.</li>
        </ul>
        <p>Finally, <span class="highlight">we will plan the appropriate manufacturing strategy to lead your market.</span></p>
        <p>We also evaluate the client's proposed investments in manufacturing to assess whether they are financially sound and consistent with both the business strategy and the manufacturing strategy of the company.</p>
      </div>
    </section>
  </main>
</body>
</html>
```